Vermilion Reel Works Web Design

COMPANY: VERMILION REEL WORKS
LOCATION: SHANGHAI, CHINA
AREA: FILM/TV DRAMA/COMMERCIALS/GAME POST PRODUCTION, SOUND DESIGN, MUSIC, and GAME.
WEB STYLE: SIMPLE, PROFESSIONAL, TRUSTWORTHY

LANGUAGE: ENGLISH, CHINESE. (Same layout, different language)
UPDATE: AFTER PROJECT FINISHED, WE NEED UPDATE BY OURSELVES.

MAIN SUBJECT: 6
1 HOMEPAGE
2 ABOUT US
3 TEAM
4 SERVICES
5 FACILITY
6 CONTACT

add one page of JOB OPPORTUNITIES.

DETAILS
1 HOMEPAGE
SLOGAN: Vermilion Reel Works provides a well-designed working environment which amplifies your team’s ability to reach their creative goals.

Our services include:
 Feature Films
 Music & Scoring
 Commercials
 ADR & Foley
 Sound & Picture Editorial
 Sound Design
 Video Game

2 ABOUT US
Vermilion Reel Works is located in the premiere South-Bund area of Shanghai. Occupying a 5000 square meter Technical Building, Vermilion Reel Works was built by a filmmaker for filmmakers, and is one of the largest, most versatile full-service post-production facilities in China.

Vermilion Reel Works is positioning to be at the forefront of the latest technology. Our goal is to provide a comprehensive solution for the post-production needs of our clients. We offer two fully-equipped dubbing stages (one of which will be certified KESTRON VOXAR PREMIERE), a large variety of both picture and sound editing rooms, impressive Foley and ADR stages, a world-class scoring stage, and complete audio and video transfer services.

We can handle your entire project from editing all the way to the end of the final sound mix; all under one extremely comfortable roof. We fully realize that the true art is in listening to the needs of our clients and making their greatest vision a reality. To this end our creative team's expertise, with a network of sound supervisors, editors and mixers, will deliver the magic you need. Producers and directors will also find our richly appointed guest accommodations to be a comfortable and soothing place to wind up the day. Every aspect of your project will be taken care of by a skilled and dedicated team, in the way that is best suited to you.

3 TEAM
(attachment 01)

4 SERVICES
Sound Mix
ADR
FOLEY
MUSIC
Sound Design
Sound Edit
Picture Edit
for all the Films, TV Drama, Commercials, Video Games, Online Media
(attachment 02, use photo)

5 FACILITY
(attachment 03)

6 CONTACT
(attachment04)
with map

Project Deadline Extended
Reason: Designers work are great, my bosses will spend 1-2 days select one of these web design, and spend 1-2 days to make some change, maybe use new photos.

```html
<!DOCTYPE html>
<html lang="en">
<head>
<meta charset="utf-8">
<title>Vermilion Reel Works</title>
<link href="https://fonts.googleapis.com/css2?family=Fjalla+One&family=Open+Sans:wght@400;600;700&family=Oswald:wght@600&display=swap" rel="stylesheet">
<style>
:root{
  --red:#d9202e;
  --orange:#d9532a;
  --dark:#121212;
  --grey-text:#2a2a2a;
  --light-bg:#efeeed;
  --white:#ffffff;
  --muted:#6b6b6b;
  --frame:#5f5f60;
  --hilite:#4d4d4f;
}
*{margin:0;padding:0;box-sizing:border-box}
html,body{width:960px;height:1200px;overflow:hidden}
body{position:relative;background:var(--white);font-family:Arial,Helvetica,sans-serif;color:var(--grey-text)}
.abs{position:absolute}

.hero-bg{left:0;top:0;width:960px;height:370px;
  background:radial-gradient(ellipse at 8% 40%,#6b5a1c 0%,transparent 35%),
             radial-gradient(ellipse at 92% 30%,#7a6a20 0%,transparent 30%),
             linear-gradient(180deg,#1d1d1c 0%,#2e2a22 60%,#3a3428 100%)}
.top-bar{left:0;top:0;width:960px;height:65px;background:rgba(18,18,18,.92)}
.brand{left:80px;top:14px;font-family:'Fjalla One',sans-serif;font-size:28px;color:#9a9a9a;letter-spacing:.3px;line-height:36px}
.main-nav{left:434px;top:18px;display:flex;align-items:center;font-size:10.5px;color:var(--white)}
.main-nav span{padding:0 8px;line-height:25px;white-space:nowrap}
.main-nav .sep{padding:0 6px}
.main-nav .active{background:var(--orange);padding:0 14px}

.slogan{left:100px;top:72px;width:780px;text-align:center;font-family:'Open Sans',sans-serif;font-weight:600;font-size:18px;line-height:23px;color:var(--white);text-shadow:0 1px 3px #000}

.light-band{left:0;top:370px;width:960px;height:331px;background:var(--light-bg)}
.photo-frame{left:95px;top:125px;width:800px;height:308px;background:var(--frame)}
.photo-main{left:103px;top:132px;width:784px;height:294px;
  background:linear-gradient(100deg,#3a1820 0%,#7b2a3c 30%,#2a1f24 50%,#8a3045 70%,#2b1a1c 100%)}

.heading-red{font-family:'Fjalla One',sans-serif;font-size:21px;color:var(--red);line-height:26px}
.welcome-title{left:94px;top:450px}
.speaker{left:97px;top:491px;width:144px;height:143px;border:1px solid #bbb;
  background:radial-gradient(circle at 45% 60%,#5a5048 0%,#1f1c1a 40%,#3b342e 70%,#201d1b 100%)}
.copy{font-size:9.8px;line-height:16px;color:var(--grey-text)}
.copy p+p{margin-top:16px}
.welcome-copy-a{left:254px;top:492px;width:340px}
.welcome-copy-b{left:96px;top:645px;width:500px}
.divider{left:609px;top:455px;height:225px;border-left:1px dotted #b5b5b5}

.services-title{left:630px;top:450px}
.service-list{left:630px;top:481px;width:250px;list-style:none;font-family:'Open Sans',sans-serif;font-size:12px;color:var(--muted)}
.service-list li{height:30.4px;line-height:30.4px;padding-left:19px;position:relative}
.service-list li::before{content:"";position:absolute;left:7px;top:12px;border-left:6px solid #a5a5a5;border-top:3.5px solid transparent;border-bottom:3.5px solid transparent}
.service-list li.current{background:var(--hilite);color:var(--white)}
.service-list li.current::before{border-left-color:var(--white)}

.section-title{font-family:'Oswald',sans-serif;font-weight:600;font-size:16px;letter-spacing:-.6px;color:#1b1b1b;line-height:20px}
.producers-title{left:87px;top:711px}
.arrows{display:flex;gap:5px}
.arrows svg{display:block}
.producers-arrows{left:843px;top:716px}

.card{top:742px;width:155px;height:150px;background:var(--white);border:1px solid #dedede;box-shadow:0 1px 3px rgba(0,0,0,.12)}
.card-img{width:100%;height:91px}
.card h3,.entry h3{font-family:'Open Sans',sans-serif;font-weight:400;font-size:11px;color:var(--orange);letter-spacing:-.5px}
.card h3{margin:8px 0 0 10px}
.card p{margin:4px 0 0 10px;font-size:9.8px;line-height:13px;color:#3a3a3a}

.events-band{left:82px;top:930px;width:470px;height:30px;background:linear-gradient(90deg,#f4f4f4,#fff)}
.events-title{left:90px;top:936px}
.events-arrows{left:521px;top:938px}
.musicians-title{left:576px;top:936px}
.musicians-arrows{left:843px;top:938px}
.panel{top:965px;height:150px;background:var(--white);border:1px solid #dcdcdc;box-shadow:0 1px 4px rgba(0,0,0,.12)}
.entry{position:absolute;left:0;width:100%}
.date{position:absolute;left:9px;width:52px;height:52px;background:var(--orange);color:var(--white);text-align:center;font-family:'Open Sans',sans-serif}
.date b{display:block;font-size:23px;line-height:27px;margin-top:2px}
.date i{display:block;font-style:normal;font-weight:700;font-size:10px;line-height:12px}
.entry h3{position:absolute;top:0}
.entry p{position:absolute;top:19px;font-size:9.6px;line-height:13px;color:#3a3a3a}
.portrait{position:absolute;left:9px;width:52px;height:52px;background:linear-gradient(180deg,#d8d8d8,#8a7766 60%,#6a6a6a)}

.footer{left:0;top:1138px;width:960px;height:62px;background:#1a1a1b}
.footer-brand{left:104px;top:1156px;font-family:'Fjalla One',sans-serif;font-size:24px;color:#4a4a4a;line-height:30px}
.footer-nav{left:494px;top:1155px;display:flex;font-size:10.5px;color:#e0e0e0}
.footer-nav span{padding:0 7px}
.footer-nav span:first-child{padding-left:0}
.copyright{left:702px;top:1175px;font-size:10px;color:#e0e0e0}
</style>
</head>
<body>

<div class="abs hero-bg" role="img" aria-label="Blurred mixing console lights behind the header"></div>
<div class="abs top-bar"></div>
<div class="abs brand">VERMILION REEL WORKS</div>
<nav class="abs main-nav">
  <span class="active">HOME</span>
  <span>ABOUT US</span><span class="sep">|</span>
  <span>TEAM</span><span class="sep">|</span>
  <span>SERVICES</span><span class="sep">|</span>
  <span>FACILITY</span><span class="sep">|</span>
  <span>CONTACT</span>
</nav>

<p class="abs slogan">Vermilion Reel Works provides a well-designed working environment which amplifies your team’s ability to reach their creative goals.</p>

<div class="abs light-band"></div>
<div class="abs photo-frame"></div>
<div class="abs photo-main" role="img" aria-label="Photo of a group of musicians celebrating with a guitar under red stage light"></div>

<h2 class="abs heading-red welcome-title">Welcome to Vermilion Reel Works.</h2>
<div class="abs speaker" role="img" aria-label="Photo of studio monitor speakers"></div>
<div class="abs copy welcome-copy-a">
  <p>Lorem ipsum dolor sit amet, consectetur adipiscing elit. Quisque dapibus accumsan orci, pretium eleifend arcu adipiscing eget. Fusce accumsan facilisis tincidunt. Phasellus tempor enim purus, vitae venenatis est. Ut imperdiet hendrerit pulvinar. Cras at tellus a enim condimentum mollis ut et tellus.</p>
  <p>Mauris dolor magna, elementum eu dictum eu, fermentum a nibh. Praesent ut dui lectus, vel lacinia sem. Praesent commodo malesuada urna, quis convallis risus dictum et.</p>
</div>
<div class="abs copy welcome-copy-b">
  <p>Lorem ipsum dolor sit amet, consectetur adipiscing elit. Quisque dapibus accumsan orci, pretium eleifend arcu adipiscing eget. Fusce accumsan facilisis tincidunt. Phasellus tempor enim purus, vitae venenatis est. Ut imperdiet hendrerit pulvinar.</p>
</div>
<div class="abs divider"></div>

<h2 class="abs heading-red services-title">The services i provide are:</h2>
<ul class="abs service-list">
  <li>Feature Films</li>
  <li class="current">Music &amp; Scoring</li>
  <li>Commercials</li>
  <li>ADR &amp; Foley</li>
  <li>Sound &amp; Picture Editorial</li>
  <li>Sound Design</li>
  <li>Video Game</li>
</ul>

<h2 class="abs section-title producers-title">MUSIC PRODUCERS</h2>
<div class="abs arrows producers-arrows">
  <svg width="13" height="13" viewBox="0 0 13 13"><circle cx="6.5" cy="6.5" r="6.5" fill="#d9532a"/><path d="M8 3.5 4.5 6.5 8 9.5z" fill="#fff"/></svg>
  <svg width="13" height="13" viewBox="0 0 13 13"><circle cx="6.5" cy="6.5" r="6.5" fill="#d9532a"/><path d="M5 3.5 8.5 6.5 5 9.5z" fill="#fff"/></svg>
</div>

<div class="abs card" style="left:86px">
  <div class="card-img" role="img" aria-label="Photo of rack audio interface with lit knobs" style="background:linear-gradient(180deg,#2c2c2c,#7a7a6a 50%,#3a3a3a)"></div>
  <h3>Lorem Ipsum</h3>
  <p>Lorem ipsum dolor sit amet, consectetuer adipiscing elit</p>
</div>
<div class="abs card" style="left:293px">
  <div class="card-img" role="img" aria-label="Photo of a large mixing desk" style="background:linear-gradient(170deg,#2b3a44,#1c2228 55%,#4a5a50)"></div>
  <h3>Lorem Ipsum</h3>
  <p>Lorem ipsum dolor sit amet, consectetuer adipiscing elit</p>
</div>
<div class="abs card" style="left:509px">
  <div class="card-img" role="img" aria-label="Photo of a control surface and keyboard on a wooden desk" style="background:linear-gradient(180deg,#2a2418,#8a6a2a 55%,#c8b38a)"></div>
  <h3>Lorem Ipsum</h3>
  <p>Lorem ipsum dolor sit amet, consectetuer adipiscing elit</p>
</div>
<div class="abs card" style="left:717px">
  <div class="card-img" role="img" aria-label="Photo of an engineer working at a studio console" style="background:linear-gradient(180deg,#8a6a44,#5a4430 55%,#2e2622)"></div>
  <h3>Lorem Ipsum</h3>
  <p>Lorem ipsum dolor sit amet, consectetuer adipiscing elit</p>
</div>

<div class="abs events-band"></div>
<h2 class="abs section-title events-title">EVENTS</h2>
<div class="abs arrows events-arrows">
  <svg width="13" height="13" viewBox="0 0 13 13"><circle cx="6.5" cy="6.5" r="6.5" fill="#d9532a"/><path d="M8 3.5 4.5 6.5 8 9.5z" fill="#fff"/></svg>
  <svg width="13" height="13" viewBox="0 0 13 13"><circle cx="6.5" cy="6.5" r="6.5" fill="#d9532a"/><path d="M5 3.5 8.5 6.5 5 9.5z" fill="#fff"/></svg>
</div>
<h2 class="abs section-title musicians-title">NEWEST MUSICIANS</h2>
<div class="abs arrows musicians-arrows">
  <svg width="13" height="13" viewBox="0 0 13 13"><circle cx="6.5" cy="6.5" r="6.5" fill="#d9532a"/><path d="M8 3.5 4.5 6.5 8 9.5z" fill="#fff"/></svg>
  <svg width="13" height="13" viewBox="0 0 13 13"><circle cx="6.5" cy="6.5" r="6.5" fill="#d9532a"/><path d="M5 3.5 8.5 6.5 5 9.5z" fill="#fff"/></svg>
</div>

<section class="abs panel" style="left:82px;width:470px">
  <div class="entry" style="top:13px">
    <div class="date" style="top:0"><b>29</b><i>OCT</i></div>
    <h3 style="left:73px">Lorem Ipsum</h3>
    <p style="left:73px;width:390px">Lorem ipsum dolor sit amet, Lorem ipsum dolor sit amet, consectetuer adipiscing elitcon sectetuer. sit amet, consectetuer adipiscing elitconsectetuer.sit amet, consectetuer adipi-scing elitconsectetuer.</p>
  </div>
  <div class="entry" style="top:80px">
    <div class="date" style="top:0"><b>29</b><i>OCT</i></div>
    <h3 style="left:73px">Lorem Ipsum</h3>
    <p style="left:73px;width:390px">Lorem ipsum dolor sit amet, Lorem ipsum dolor sit amet, consectetuer adipiscing elitcon sectetuer. sit amet, consectetuer adipiscing elitconsectetuer.sit amet, consectetuer adipi-scing elitconsectetuer.</p>
  </div>
</section>

<section class="abs panel" style="left:570px;width:305px">
  <div class="entry" style="top:13px">
    <div class="portrait" style="top:0" role="img" aria-label="Portrait photo of a musician"></div>
    <h3 style="left:69px">Lorem Ipsum</h3>
    <p style="left:69px;width:230px">Lorem ipsum dolor sit amet, Lorem ipsum dolor sit amet, consectetuer adipiscing elitconsectetuer.</p>
  </div>
  <div class="entry" style="top:79px">
    <div class="portrait" style="top:0" role="img" aria-label="Portrait photo of a musician"></div>
    <h3 style="left:69px">Lorem Ipsum</h3>
    <p style="left:69px;width:230px">Lorem ipsum dolor sit amet, Lorem ipsum dolor sit amet, consectetuer adipiscing elitconsectetuer.</p>
  </div>
</section>

<footer class="abs footer"></footer>
<div class="abs footer-brand">VERMILION REEL WORKS</div>
<nav class="abs footer-nav">
  <span>HOME</span><span>|</span><span>ABOUT US</span><span>|</span><span>TEAM</span><span>|</span><span>SERVICES</span><span>|</span><span>FACILITY</span><span>|</span><span>CONTACT</span>
</nav>
<div class="abs copyright">© 2014 VERMILION REEL WORKS. ALL</div>

</body>
</html>
```